Visitenkarten-Design für Boutique-Unternehmensberatung
Zielgruppe
Boutique Unternehmensberatung für die Chemische Industrie. Wir unterstützen Unternehmen, die Beziehung zu Ihren Händlern zu optimieren.
Vorläufige Website handelsbruecke-nord.de kann ggf weitere Einblicke geben. Hinweis: Diese Website wurde bisher noch nicht professionell erstellt.
Aufgabenstellung
Die Visitenkarte sollte vertrauenserweckend und seriös wirken. Zeitgleich aber auch modern.

```html
<!DOCTYPE html>
<html lang="de">
<head>
<meta charset="utf-8">
<title>Visitenkarte – Handelsbrücke Nord</title>
<link rel="stylesheet" href="https://fonts.googleapis.com/css2?family=Poppins:wght@400;500;600;700&display=swap">
<style>
  :root {
    --brand-blue: #306b96;
    --brand-blue-dark: #25587d;
    --paper: #f7f4ec;
    --stage: #eceef1;
    --ink: #2b4f6b;
    --white: #ffffff;
    --photo-a: #c9b8a6;
    --photo-b: #8e9aa6;
  }
  * { box-sizing: border-box; margin: 0; padding: 0; }
  html, body {
    width: 1200px; height: 413px; overflow: hidden;
    background: var(--stage);
    font-family: "Poppins", sans-serif;
  }
  .stage {
    position: relative; width: 1200px; height: 413px;
    display: flex; justify-content: center; align-items: center; gap: 60px;
  }
  .card {
    position: relative; width: 540px; height: 320px; overflow: hidden;
    border-radius: 4px;
    box-shadow: 0 6px 18px rgba(30, 45, 60, 0.18);
  }

  /* Front */
  .card--front { background: var(--brand-blue); display: flex; align-items: center; justify-content: center; }
  .wordmark { display: flex; align-items: center; gap: 12px; color: var(--white); font-weight: 600; }
  .wordmark__dot { width: 30px; height: 30px; border-radius: 50%; background: var(--white); flex: none; }
  .wordmark__name { font-size: 30px; line-height: 1.05; letter-spacing: 0.2px; }

  /* Back */
  .card--back { background: var(--paper); color: var(--ink); }
  .back__band { position: absolute; left: 0; top: 0; width: 540px; height: 160px; }
  .back__header { position: absolute; left: 26px; top: 24px; right: 20px; color: var(--white); }
  .back__title { display: flex; align-items: baseline; gap: 10px; white-space: nowrap; }
  .back__name { font-size: 24px; font-weight: 700; }
  .back__role { font-size: 12px; font-weight: 500; }
  .back__direct { display: flex; gap: 18px; margin-top: 6px; font-size: 10px; white-space: nowrap; }
  .back__direct span, .contact li { display: flex; align-items: center; gap: 6px; }
  .back__photo {
    position: absolute; left: 206px; top: 102px; width: 76px; height: 76px; border-radius: 50%;
    border: 3px solid var(--white);
    background: radial-gradient(circle at 45% 40%, var(--photo-a), var(--photo-b));
  }
  .company { position: absolute; left: 308px; top: 116px; font-size: 10.5px; line-height: 1.45; font-style: normal; }
  .company__name { font-weight: 700; color: var(--brand-blue-dark); }
  .contact { position: absolute; left: 308px; top: 196px; list-style: none; font-size: 10.5px; line-height: 1.9; }
  .icon { width: 12px; height: 12px; flex: none; }
  .back__wordmark {
    position: absolute; left: 26px; bottom: 36px; display: flex; align-items: center; gap: 8px;
    color: var(--brand-blue); font-weight: 600;
  }
  .back__wordmark .wordmark__dot { width: 16px; height: 16px; background: var(--brand-blue); }
  .back__wordmark .wordmark__name { font-size: 15px; }
</style>
</head>
<body>
<main class="stage">

  <section class="card card--front" aria-label="Vorderseite">
    <div class="wordmark">
      <span class="wordmark__dot"></span>
      <span class="wordmark__name">Handelsbrücke<br>Nord</span>
    </div>
  </section>

  <section class="card card--back" aria-label="Rückseite">
    <svg class="back__band" viewBox="0 0 540 160" preserveAspectRatio="none" aria-hidden="true">
      <path d="M0 0 H540 V80 C420 88 260 118 0 152 Z" fill="var(--brand-blue)"/>
    </svg>

    <header class="back__header">
      <div class="back__title">
        <span class="back__name">Jonas Albrecht</span>
        <span class="back__role">• Geschäftsführer / CEO</span>
      </div>
      <div class="back__direct">
        <span>
          <svg class="icon" viewBox="0 0 12 12"><circle cx="6" cy="6" r="6" fill="#fff"/><path d="M4 3.2l1 1.4-.6.7a4 4 0 002.3 2.3l.7-.6 1.4 1-.6 1A5 5 0 013 4z" fill="var(--brand-blue)"/></svg>
          +49 0151 / 12 34 56 78
        </span>
        <span>
          <svg class="icon" viewBox="0 0 12 12"><circle cx="6" cy="6" r="6" fill="#fff"/><rect x="3" y="4" width="6" height="4.2" fill="none" stroke="var(--brand-blue)" stroke-width=".9"/><path d="M3 4l3 2.3L9 4" fill="none" stroke="var(--brand-blue)" stroke-width=".9"/></svg>
          j.albrecht@handelsbruecke-nord.de
        </span>
      </div>
    </header>

    <div class="back__photo" role="img" aria-label="Porträtfoto von Jonas Albrecht"></div>

    <address class="company">
      <div class="company__name">HBN Handelsbrücke Nord<br>GmbH</div>
      <div>Hafenstraße 12</div>
      <div>20457 Hamburg</div>
    </address>

    <ul class="contact">
      <li>
        <svg class="icon" viewBox="0 0 12 12"><circle cx="6" cy="6" r="6" fill="var(--brand-blue)"/><path d="M4 3.2l1 1.4-.6.7a4 4 0 002.3 2.3l.7-.6 1.4 1-.6 1A5 5 0 013 4z" fill="#fff"/></svg>
        +49 0151 / 12 34 56 78
      </li>
      <li>
        <svg class="icon" viewBox="0 0 12 12"><circle cx="6" cy="6" r="6" fill="var(--brand-blue)"/><rect x="3" y="4" width="6" height="4.2" fill="none" stroke="#fff" stroke-width=".9"/><path d="M3 4l3 2.3L9 4" fill="none" stroke="#fff" stroke-width=".9"/></svg>
        info@handelsbruecke-nord.de
      </li>
      <li>
        <svg class="icon" viewBox="0 0 12 12"><circle cx="6" cy="6" r="6" fill="var(--brand-blue)"/><circle cx="6" cy="6" r="3.2" fill="none" stroke="#fff" stroke-width=".8"/><path d="M2.8 6h6.4M6 2.8c-1.5 2-1.5 4.4 0 6.4M6 2.8c1.5 2 1.5 4.4 0 6.4" fill="none" stroke="#fff" stroke-width=".7"/></svg>
        www.handelsbruecke-nord.de
      </li>
    </ul>

    <div class="back__wordmark">
      <span class="wordmark__dot"></span>
      <span class="wordmark__name">Handelsbrücke<br>Nord</span>
    </div>
  </section>

</main>
</body>
</html>
```